Business Card Admin Services

I have just selected a new logo. Now I need a business card.

The business is contract administrative services. We provide high value administrative services to small businesses/offices. We are professional, efficient, but also have fun and energetic personalities.

Lora Pike
Lora@DeskFalcon.ca
604-913-4078
DeskFalcon.ca

I will also want Facebook, Twitter and LinkedIn icons on the card - please up my "handles" beside each.
Facebook is DeskFalconCanada
Twitter is @DFalconLora
LinkedIn is LoraPikeDeskFalcon
Updates

New logo just updated.  Thanks for your patience!

Target Market(s)

Small businesses, professional offices

Industry/Entity Type

Business

Requirements
Must have
• bold, fun use of my colours
font needs to be consistent with the logo
Nice to have
• I quite like a closeup of the head

```html
<!DOCTYPE html>
<html lang="en">
<head>
<meta charset="utf-8">
<title>Desk Falcon – Business Card</title>
<link rel="stylesheet" href="https://fonts.googleapis.com/css2?family=Arimo:wght@400;700&family=Raleway:wght@300&display=swap">
<style>
  :root {
    --pink: #ec0b84;
    --black: #111111;
    --white: #ffffff;
    --backdrop: #bdbdbd;
    --card-w: 560px;
    --card-h: 320px;
  }
  * { box-sizing: border-box; margin: 0; padding: 0; }
  html, body {
    width: 1200px; height: 900px; overflow: hidden;
    background: var(--backdrop);
    font-family: "Arimo", Arial, sans-serif;
  }
  .stage {
    width: 1200px; height: 900px;
    display: flex; flex-direction: column; align-items: center; justify-content: center;
    gap: 50px;
  }
  .card {
    position: relative;
    width: var(--card-w); height: var(--card-h);
    overflow: hidden;
    box-shadow: 0 4px 14px rgba(0,0,0,0.18);
  }

  /* Front */
  .card-front {
    background: var(--pink);
    display: flex; flex-direction: column; align-items: center; justify-content: center;
  }
  .brand-dot {
    width: 104px; height: 104px; border-radius: 50%;
    background: var(--black);
  }
  .brand-name {
    font-family: "Raleway", "Arimo", sans-serif;
    font-weight: 300;
    letter-spacing: 1px;
    text-transform: uppercase;
    line-height: 1;
  }
  .card-front .brand-name {
    color: var(--black);
    font-size: 38px;
    margin-top: 14px;
  }
  .front-url {
    color: var(--white);
    font-size: 12px;
    letter-spacing: 3.5px;
    margin-top: 16px;
  }

  /* Back */
  .card-back { background: var(--white); }
  .back-brand {
    position: absolute; top: 26px; left: 0; right: 0;
    display: flex; flex-direction: column; align-items: center;
  }
  .back-brand .brand-dot {
    width: 50px; height: 50px; background: var(--pink);
  }
  .back-brand .brand-name {
    color: var(--black);
    font-size: 23px;
    margin-top: 8px;
  }
  .contact {
    position: absolute; top: 134px; left: 0; right: 0;
    display: flex; justify-content: center;
  }
  .contact-person {
    width: 260px; padding-right: 14px;
    text-align: right;
    color: var(--black);
    font-size: 13px; line-height: 1.3;
    border-right: 1.5px solid var(--black);
  }
  .person-name { font-size: 15px; text-transform: uppercase; margin-top: 30px; }
  .person-role { font-size: 12px; }
  .person-lines { margin-top: 16px; }
  .contact-company {
    width: 260px; padding-left: 14px;
    color: var(--pink);
    font-size: 13px; line-height: 1.3;
  }
  .company-web { margin-top: 10px; }
  .social-list { list-style: none; margin-top: 6px; }
  .social-item {
    display: flex; align-items: center; gap: 7px;
    line-height: 17px;
  }
  .social-mark {
    width: 10px; height: 10px;
    background: var(--pink);
    flex: none;
  }
  .band-black {
    position: absolute; left: 0; bottom: 0;
    width: 62%; height: 10px;
    background: var(--black);
  }
  .band-pink {
    position: absolute; right: 0; bottom: 0;
    width: 38%; height: 30px;
    background: var(--pink);
  }
</style>
</head>
<body>
  <main class="stage">
    <section class="card card-front" aria-label="Card front">
      <div class="brand-dot"></div>
      <div class="brand-name">Desk Falcon</div>
      <div class="front-url">www.DeskFalcon.ca</div>
    </section>

    <section class="card card-back" aria-label="Card back">
      <div class="back-brand">
        <div class="brand-dot"></div>
        <div class="brand-name">Desk Falcon</div>
      </div>
      <div class="contact">
        <div class="contact-person">
          <p class="person-name">Lora Pike</p>
          <p class="person-role">Administrator</p>
          <div class="person-lines">
            <p>604-913-4078</p>
            <p>Lora@DeskFalcon.ca</p>
          </div>
        </div>
        <div class="contact-company">
          <p>Suite 00, 000 Sample Road,<br>Vancouver BC V0V 0V0</p>
          <p class="company-web">www.DeskFalcon.ca</p>
          <ul class="social-list">
            <li class="social-item"><span class="social-mark"></span>DeskFalconCanada</li>
            <li class="social-item"><span class="social-mark"></span>@DFalconLora</li>
            <li class="social-item"><span class="social-mark"></span>LoraPikeDeskFalcon</li>
          </ul>
        </div>
      </div>
      <div class="band-black"></div>
      <div class="band-pink"></div>
    </section>
  </main>
</body>
</html>
```